Industrial Automation company requires a business card design

Valtrin Automation provides design & build of Automated Equipment for manufacturing industry.
www.valtrinautomation.example
The equipment we design is used for manufacturing in sectors such as medical device, pharmaceutical, aerospace and electronics.
We require a new business card design which incorporates our (New) logo and the key message words:
Automated Equipment:
Design, Build, Control, Test, Support

```html
<!DOCTYPE html>
<html lang="en">
<head>
<meta charset="utf-8">
<title>Valtrin Automation — Business Card</title>
<link href="https://fonts.googleapis.com/css2?family=Open+Sans:wght@400;600;700&display=swap" rel="stylesheet">
<style>
  :root{
    --bg:#e9e7e3;
    --paper:#ffffff;
    --paper-shade:#eeeeee;
    --green:#1aa557;
    --green-dark:#11894a;
    --charcoal:#2c2c2c;
    --charcoal-deep:#1f1f1f;
    --ink:#222222;
    --white:#ffffff;
  }
  *{margin:0;padding:0;box-sizing:border-box}
  html,body{width:1200px;height:892px;overflow:hidden}
  body{
    background:var(--bg);
    font-family:"Open Sans",Arial,sans-serif;
    display:flex;align-items:center;justify-content:center;gap:40px;
  }
  .card{
    position:relative;width:560px;height:320px;
    background:linear-gradient(135deg,var(--paper) 40%,var(--paper-shade));
    box-shadow:0 6px 18px rgba(0,0,0,.18);
    overflow:hidden;
  }
  .card-bands{position:absolute;inset:0;width:100%;height:100%}
  .brand{
    position:absolute;display:flex;align-items:center;gap:12px;
  }
  .brand-dot{width:34px;height:34px;border-radius:50%;background:var(--green);flex:none}
  .brand-name{
    font-weight:700;font-size:24px;color:var(--ink);letter-spacing:.5px;white-space:nowrap;
  }
  .card-front .brand{left:30px;top:42px}
  .person{position:absolute;right:34px;top:40px;text-align:left}
  .person-name{font-weight:700;font-size:23px;color:var(--ink);line-height:1.1}
  .person-role{font-size:16px;color:var(--green);line-height:1.3}
  .contacts{
    position:absolute;left:335px;top:186px;list-style:none;
    color:var(--white);font-size:13.5px;
  }
  .contacts li{display:flex;align-items:center;gap:10px;height:26px}
  .contacts svg{width:16px;height:16px;flex:none}
  .services{
    position:absolute;left:26px;top:178px;list-style:none;
    color:var(--white);font-size:13px;line-height:21px;
  }
  .services li{display:flex;gap:8px}
  .services li::before{content:"★";font-size:11px}
  .services .cont{padding-left:19px}
  .services .cont::before{content:none}
  .card-back .brand{left:50%;top:50%;transform:translate(-50%,-50%)}
  .card-back .brand-name{font-size:34px}
  .card-back .brand-dot{width:44px;height:44px}
</style>
</head>
<body>
  <section class="card card-front">
    <svg class="card-bands" viewBox="0 0 560 320" preserveAspectRatio="none" aria-hidden="true">
      <rect x="250" y="146" width="310" height="174" fill="var(--green)"/>
      <polygon points="0,160 262,160 346,320 0,320" fill="var(--charcoal)"/>
    </svg>
    <div class="brand">
      <span class="brand-dot"></span>
      <span class="brand-name">Valtrin Automation</span>
    </div>
    <div class="person">
      <div class="person-name">Darren Kilmore</div>
      <div class="person-role">Senior Partner</div>
    </div>
    <ul class="services">
      <li>Process/Concept development</li>
      <li>Bespoke Mechanical Design</li>
      <li>Electrical Design &amp; Specification</li>
      <li>Control Software &amp; Human Machine</li>
      <li class="cont">Interface development</li>
      <li>Equipment integration</li>
    </ul>
    <ul class="contacts">
      <li>
        <svg viewBox="0 0 16 16"><rect width="16" height="16" fill="var(--white)"/><path d="M5 3.5l2 2.2-1 1.2a6 6 0 0 0 3.1 3.1l1.2-1 2.2 2-1.2 1.6C7.4 12.4 3.6 8.6 3.4 4.7z" fill="var(--green)"/></svg>
        00 353 (0) 55 01234
      </li>
      <li>
        <svg viewBox="0 0 16 16"><rect width="16" height="16" fill="var(--white)"/><rect x="3" y="5" width="10" height="7" fill="none" stroke="var(--green)" stroke-width="1.3"/><path d="M3 5l5 4 5-4" fill="none" stroke="var(--green)" stroke-width="1.3"/></svg>
        00 353 (0) 55 01240
      </li>
      <li>
        <svg viewBox="0 0 16 16"><rect width="16" height="16" fill="var(--white)"/><circle cx="8" cy="8" r="4.5" fill="none" stroke="var(--green)" stroke-width="1.3"/><path d="M3.5 8h9M8 3.5v9" stroke="var(--green)" stroke-width="1"/></svg>
        dkilmore@valtrin.example
      </li>
    </ul>
  </section>

  <section class="card card-back">
    <div class="brand">
      <span class="brand-dot"></span>
      <span class="brand-name">Valtrin Automation</span>
    </div>
  </section>
</body>
</html>
```